Willow Harbor Family Relief-buis card/stationary design for our non profit company
Have fun, be creative and lets see what you come up with!
Willow Harbor Family Relief-buis card/stationary design for our non profit company - Health
Creative Brief
Bright & Fun-filled
Dana Holloway
27415 Marlow Ave Ste#208 Tustin CA 92781
harborwr@brightpostmail.net
We have not yet decided our titles yet. In the meantime please focus on the design. Once we choose the design we want, we will ask you to put our names,title etc. Thank you!
Please put our tagline: "Supporting the care in caregiving" on the back of the card.

```html
<!DOCTYPE html>
<html lang="en">
<head>
<meta charset="utf-8">
<title>Willow Harbor Family Relief – Business Card</title>
<link href="https://fonts.googleapis.com/css2?family=Open+Sans:wght@400;600&display=swap" rel="stylesheet">
<style>
  :root{
    --page-bg:#e4e6ea;
    --card-white:#ffffff;
    --card-grey:#e9eaec;
    --brand-blue:#1d5cab;
    --brand-navy:#173f86;
    --swoosh-grey:#b9bcc2;
    --text-grey:#5b5f66;
  }
  *{margin:0;padding:0;box-sizing:border-box}
  html,body{width:1200px;height:901px;overflow:hidden;background:var(--page-bg)}
  .canvas{position:relative;width:1200px;height:901px}
  .business-card{
    position:absolute;left:150px;top:193px;width:900px;height:514px;
    border-radius:34px;overflow:hidden;
    background:linear-gradient(160deg,var(--card-white) 35%,var(--card-grey) 100%);
    box-shadow:0 18px 40px rgba(0,0,0,.18);
  }
  .card-swoosh{position:absolute;inset:0;width:100%;height:100%}
  .brand-name{
    position:absolute;left:310px;top:130px;width:560px;
    font-family:"Open Sans",sans-serif;font-weight:600;font-size:32px;
    color:var(--brand-blue);line-height:1.2;white-space:nowrap;
  }
  .contact-list{
    position:absolute;left:38px;top:120px;list-style:none;
    font-family:"Open Sans",sans-serif;font-size:15px;color:var(--text-grey);
  }
  .contact-list li{display:flex;align-items:center;gap:12px;height:31px}
  .contact-list svg{width:15px;height:15px;fill:var(--text-grey);flex:none}
  .person{
    position:absolute;left:540px;top:314px;text-align:center;
    font-family:"Open Sans",sans-serif;
  }
  .person-name{font-size:23px;font-weight:600;color:var(--brand-navy);letter-spacing:1px;text-transform:uppercase}
  .person-title{font-size:15px;color:var(--text-grey);letter-spacing:1px;text-transform:uppercase;margin-top:2px}
</style>
</head>
<body>
<div class="canvas">
  <div class="business-card">
    <svg class="card-swoosh" viewBox="0 0 900 514" preserveAspectRatio="none" aria-hidden="true">
      <path d="M0 315 C180 400 520 430 900 355 L900 370 C520 445 180 415 0 332 Z" fill="var(--swoosh-grey)"/>
      <path d="M0 340 C200 430 560 450 900 380 L900 514 L0 514 Z" fill="var(--brand-blue)"/>
      <path d="M0 340 C200 430 560 450 900 380 L900 392 C560 462 200 445 0 356 Z" fill="var(--brand-navy)" opacity=".35"/>
    </svg>

    <ul class="contact-list">
      <li><svg viewBox="0 0 24 24"><path d="M6.6 10.8a15.1 15.1 0 0 0 6.6 6.6l2.2-2.2a1 1 0 0 1 1-.25 11.4 11.4 0 0 0 3.6.57 1 1 0 0 1 1 1V20a1 1 0 0 1-1 1A17 17 0 0 1 3 4a1 1 0 0 1 1-1h3.5a1 1 0 0 1 1 1c0 1.25.2 2.45.57 3.57a1 1 0 0 1-.25 1z"/></svg>012 345 6789</li>
      <li><svg viewBox="0 0 24 24"><path d="M7 1h10a2 2 0 0 1 2 2v18a2 2 0 0 1-2 2H7a2 2 0 0 1-2-2V3a2 2 0 0 1 2-2zm0 3v14h10V4z"/></svg>012 345 6789</li>
      <li><svg viewBox="0 0 24 24"><path d="M6 2h9v5H6zM4 9h16a2 2 0 0 1 2 2v7h-4v4H6v-4H2v-7a2 2 0 0 1 2-2zm4 8v3h8v-3z"/></svg>012 345 6789</li>
      <li><svg viewBox="0 0 24 24"><path d="M2 5h20v14H2zm2 2v.5l8 5 8-5V7z"/></svg>harborwr@brightpostmail.net</li>
      <li><svg viewBox="0 0 24 24"><path d="M12 2a10 10 0 1 0 0 20 10 10 0 0 0 0-20zm0 2c1.2 1.5 2 3.6 2.2 6H9.8C10 7.6 10.8 5.5 12 4zm-2.2 8h4.4c-.2 2.4-1 4.5-2.2 6-1.2-1.5-2-3.6-2.2-6z"/></svg>www.harborwr.org</li>
    </ul>

    <p class="brand-name">Willow Harbor Family Relief</p>

    <div class="person">
      <p class="person-name">Dana Holloway</p>
      <p class="person-title">Financial Advisor</p>
    </div>
  </div>
</div>
</body>
</html>
```